Maple Yard Fight Club's Heatwave Trim-Up Contest

Maple Yard Fight Club Presents
“The Heatwave Trim-Up Showdown”
Win the fight for fitness and take home awesome prizes.
1st Place Tabby Lite (16gb) (value $299)
2nd Place One-Month All Access Membership (value $199)
3rd Place Maple Yard Fight Club Training Gloves, T-Shirt and Handwraps (value $79)
(fine print)
* Men’s & Women’s Divisions – two sets of prizes.
* Contestants must register between June 10th and June 15th. Entry fee is $25.
* At registration, contestants will be required to weigh-in in a private setting. For the duration of the competition, actual weight will not be posted; only percent gain or loss.
* Results are based on percentage weight loss as measured on September 19th.
Note: Maple Yard Fight Club reserves the right to cancel the competition in a division if there are fewer than 10 contestants in that division. In that event, a full refund will be issued to participants in that division.

ABOUT US:
MYFC is not a traditional health club with rows of cardio equipment, weight-training machines, or overcrowded step-aerobic classes. Nor are we like old-school boxing or martial arts studios which can oftentimes be scary and uninviting.

Our goal is to strike a balance between instruction, conditioning and fun. We offer over 70 classes per week: mostly boxing, but also muay thai, mixed martial arts ("MMA"), and boot camps. All of our instructors have fought professionally or at the amateur level so they're teaching from experience, not what they learned from an online course.

Target Market(s)

Gym members.

Industry/Entity Type

Fitness

Requirements
Must have
• Our logo (attached) converted to blue.

```html
<!DOCTYPE html>
<html lang="en">
<head>
<meta charset="utf-8">
<title>Maple Yard Fight Club – Heatwave Trim-Up Contest</title>
<link rel="stylesheet" href="https://fonts.googleapis.com/css2?family=Archivo+Black&family=Black+Ops+One&family=Oswald:wght@500;700&family=Special+Elite&family=Tinos&display=swap">
<style>
  :root {
    --paper: #ffffff;
    --band-blue: #3b3b96;
    --band-text: #8c8cc6;
    --night: #1b1b3a;
    --night-deep: #0b0b26;
    --you-blue: #3e3e98;
    --vs-blue: #5656d0;
    --losers-lilac: #7c7cba;
    --cream: #ece3c8;
    --prize-red: #e01818;
    --headline-red: #ff1a1a;
    --rule: #8a8aa0;
    --logo-blue: #3a3ad8;
    --belt-black: #111114;
    --belt-gold: #d8a824;
    --url-blue: #3434c8;
  }
  html, body { margin: 0; padding: 0; overflow: hidden; background: var(--paper); }
  .poster {
    position: relative; width: 800px; height: 1200px; overflow: hidden;
    background: var(--paper);
  }
  .arena {
    position: absolute; left: 20px; top: 120px; width: 762px; height: 900px;
    background: linear-gradient(180deg, #2a2a44 0%, var(--night) 45%, var(--night-deep) 100%);
  }
  .title-band { position: absolute; left: 0; top: 0; width: 800px; height: 220px; }
  .main-event {
    position: absolute; left: -20px; top: 30px; width: 860px;
    font-family: "Black Ops One", sans-serif; font-size: 118px; letter-spacing: 6px;
    color: var(--band-text); white-space: nowrap;
    transform: rotate(-4.3deg); transform-origin: left top;
  }
  .gloves {
    position: absolute; left: 90px; top: 150px; width: 155px; height: 240px;
    background: radial-gradient(ellipse at 40% 60%, #d92424 0%, #9c1010 55%, #1a1a1a 100%);
    border-radius: 40px;
  }
  .you {
    position: absolute; left: 178px; top: 168px;
    font-family: "Archivo Black", sans-serif; font-size: 300px; line-height: 1;
    color: var(--you-blue); letter-spacing: -8px; white-space: nowrap;
    transform: scaleY(0.95); transform-origin: left top;
  }
  .vs {
    position: absolute; left: 540px; top: 298px;
    font-family: "Tinos", serif; font-size: 82px; color: var(--vs-blue);
  }
  .losers {
    position: absolute; left: 118px; top: 378px;
    font-family: "Archivo Black", sans-serif; font-size: 196px; line-height: 1;
    color: var(--losers-lilac); letter-spacing: -6px; white-space: nowrap;
    transform: scaleX(0.82); transform-origin: left top;
  }
  .contest-name {
    position: absolute; left: 0; width: 800px; top: 558px; text-align: center;
    font-family: "Special Elite", monospace; font-size: 34px; color: var(--cream);
  }
  .winner-belt {
    position: absolute; left: 20px; top: 830px; width: 410px; height: 170px;
    background: radial-gradient(ellipse at 50% 40%, rgba(120,120,170,0.35), rgba(40,40,80,0.1) 70%);
    border-radius: 30px;
  }
  .prizes { position: absolute; left: 20px; top: 630px; width: 310px; }
  .prize {
    border-top: 2px solid var(--rule);
    padding: 10px 0 12px 42px; height: 74px;
  }
  .prize:last-child { border-bottom: 2px solid var(--rule); height: 84px; }
  .prize h3 {
    margin: 0; font-family: "Special Elite", monospace; font-weight: normal;
    font-size: 20px; color: var(--prize-red);
  }
  .prize p {
    margin: 2px 0 0 10px; font-family: "Special Elite", monospace;
    font-size: 14px; line-height: 22px; color: var(--cream);
  }
  .prize .value { font-style: italic; font-size: 13px; }
  .challenge {
    position: absolute; left: 355px; width: 410px; top: 645px; text-align: center;
    font-family: "Oswald", sans-serif;
  }
  .challenge .goal { font-weight: 700; font-size: 27px; color: var(--headline-red); margin: 0; }
  .challenge .deadline {
    font-weight: 500; font-size: 33px; line-height: 44px; color: var(--cream); margin: 4px 0 0;
  }
  .challenge strong { font-weight: 700; }
  .club-name {
    position: absolute; left: 420px; top: 850px; width: 290px; text-align: center;
    font-family: "Oswald", sans-serif; font-weight: 700; font-size: 40px; line-height: 46px;
    color: var(--logo-blue); text-transform: lowercase;
  }
  .title-belt {
    position: absolute; left: 0; top: 985px; width: 800px; height: 215px;
    background:
      linear-gradient(90deg, var(--belt-black) 0 14%, transparent 14% 86%, var(--belt-black) 86%),
      linear-gradient(180deg, #f0c850 0%, var(--belt-gold) 60%, #9a7410 100%);
  }
  .site {
    position: absolute; left: 0; width: 800px; top: 1110px; text-align: center;
    font-family: "Oswald", sans-serif; font-weight: 700; font-size: 48px;
    color: var(--url-blue);
  }
</style>
</head>
<body>
<main class="poster">
  <div class="arena" role="img" aria-label="Dark textured navy backdrop"></div>

  <svg class="title-band" viewBox="0 0 800 220" aria-hidden="true">
    <polygon points="20,0 782,0 782,140 20,205" fill="var(--band-blue)"/>
  </svg>
  <div class="main-event">MAIN EVENT</div>

  <div class="you">YOU</div>
  <div class="gloves" role="img" aria-label="Pair of red boxing gloves hanging from a hook"></div>
  <div class="vs">VS</div>
  <div class="losers">LOSERS</div>

  <div class="contest-name">Heatwave Trim-Up Weight Loss Contest</div>

  <div class="winner-belt" role="img" aria-label="Faint championship winner belt"></div>

  <section class="prizes">
    <div class="prize">
      <h3>First Prize</h3>
      <p>Win a new Tabby Lite (white, 16gb)<br><span class="value">[Valued at $299]</span></p>
    </div>
    <div class="prize">
      <h3>Second Prize</h3>
      <p>Win a 1 month All Access Membership<br><span class="value">[Valued at $199]</span></p>
    </div>
    <div class="prize">
      <h3>Third Prize</h3>
      <p>Win a pair of MYFC training<br>gloves and handwraps<br><span class="value">[Valued at $69]</span></p>
    </div>
  </section>

  <section class="challenge">
    <p class="goal">ONE GOAL • 3 MONTH CHALLENGE</p>
    <p class="deadline">Lose the <strong>MOST</strong> weight by<br>September 19, 2013 and <strong>WIN!</strong></p>
  </section>

  <div class="club-name">Maple Yard<br>Fight Club</div>

  <div class="title-belt" role="img" aria-label="Gold and black championship belt"></div>
  <div class="site">www.mapleyardfight.com</div>
</main>
</body>
</html>
```